BRINDELLA EXTRA VIRGIN OLIVE OIL

I needs a design for an Australian Extra Virgin Olive Oil.

The label will go on a round clear bottle

The label size front and back is 145mm high x 60mm wide.

The important points for the design are as follows.

I want to see elegant olives on the label so that non English speaking markets can easily understand its olive oil. I want it too look classy . IT must also look Australian but I don't want to see kangaroos just colours that reflect Australia.

The mandatory info on front label will be

BRINDELLA

Cold Pressed
EXTRA VIRGIN OLIVE OIL

AUSTRALIAN

1 litre

```html
<!DOCTYPE html>
<html lang="en">
<head>
<meta charset="utf-8">
<title>Brindella Extra Virgin Olive Oil – Label</title>
<link rel="stylesheet" href="https://fonts.googleapis.com/css2?family=Tinos:ital,wght@0,400;0,700;1,400&display=swap">
<style>
  :root {
    --leaf-light: #8cc63f;
    --leaf-mid: #5e9e1e;
    --leaf-deep: #2f6a12;
    --cream: #f3e7b0;
    --frame-taupe: #a79d7d;
    --gold-light: #f7e14a;
    --gold-deep: #8a7414;
    --ink-green: #0c5a2e;
    --tan: #d9a868;
    --banner-dark: #4a4538;
    --banner-edge: #e9dfc2;
    --crest-taupe: #9a8a6e;
    --page: #ffffff;
  }
  * { margin: 0; padding: 0; box-sizing: border-box; }
  html, body { width: 1200px; height: 2902px; overflow: hidden; background: var(--page); }
  .label {
    position: relative;
    width: 1200px;
    height: 2902px;
    font-family: "Tinos", "Times New Roman", serif;
  }
  .label-shapes { position: absolute; inset: 0; }
  .text { position: absolute; white-space: nowrap; }

  .banner-name {
    left: 0; width: 1200px; top: 688px;
    text-align: center;
    font-size: 58px; font-weight: 700;
    letter-spacing: 2px;
    color: var(--banner-edge);
  }
  .panel-name {
    left: 118px; width: 957px; top: 1168px;
    text-align: center;
    font-size: 112px; font-weight: 700;
    color: var(--ink-green);
  }
  .panel-product {
    left: 630px; width: 400px;
    text-align: center;
    color: var(--ink-green);
  }
  .panel-product.extra { top: 1345px; font-size: 68px; }
  .panel-product.virgin { top: 1425px; font-size: 68px; }
  .panel-product.olive { top: 1530px; font-size: 100px; }
  .panel-product.oil { top: 1662px; font-size: 70px; }
  .panel-rule {
    position: absolute; left: 630px; width: 400px; height: 7px;
    background: var(--ink-green);
  }
  .panel-rule.upper { top: 1520px; }
  .panel-rule.lower { top: 1640px; }

  .mandatory {
    left: 0; width: 1220px;
    text-align: center;
    color: var(--tan);
  }
  .mandatory.brand { top: 2122px; font-size: 72px; font-weight: 700; }
  .mandatory.process { top: 2235px; font-size: 52px; font-style: italic; }
  .mandatory.product { top: 2314px; font-size: 66px; font-style: italic; }
  .mandatory.origin { top: 2405px; font-size: 52px; font-style: italic; }

  .volume {
    left: 141px; top: 2690px;
    font-size: 80px; font-weight: 700;
    color: var(--ink-green);
  }
</style>
</head>
<body>
<div class="label">
  <svg class="label-shapes" width="1200" height="2902" viewBox="0 0 1200 2902">
    <defs>
      <linearGradient id="body-green" x1="0" y1="0" x2="0" y2="1">
        <stop offset="0" stop-color="var(--leaf-deep)"/>
        <stop offset="0.45" stop-color="var(--leaf-mid)"/>
        <stop offset="1" stop-color="var(--leaf-deep)"/>
      </linearGradient>
      <linearGradient id="panel-gold" x1="1" y1="0" x2="0" y2="1">
        <stop offset="0" stop-color="var(--gold-light)"/>
        <stop offset="0.5" stop-color="#c9b22a"/>
        <stop offset="1" stop-color="var(--gold-deep)"/>
      </linearGradient>
      <linearGradient id="crest-tone" x1="0" y1="0" x2="0" y2="1">
        <stop offset="0" stop-color="#b7a886"/>
        <stop offset="1" stop-color="var(--crest-taupe)"/>
      </linearGradient>
      <radialGradient id="olive-tone" cx="0.4" cy="0.5" r="0.6">
        <stop offset="0" stop-color="#a6d23a"/>
        <stop offset="1" stop-color="#4c8a1a" stop-opacity="0.9"/>
      </radialGradient>
    </defs>

    <path class="arch-outer" d="M0 2902 V600 A600 600 0 0 1 1200 600 V2902 Z" fill="var(--leaf-light)"/>
    <path class="arch-cream" d="M20 2902 V600 A580 580 0 0 1 1180 600 V2902 Z" fill="var(--cream)"/>
    <path class="arch-body" d="M40 2902 V640 A560 600 0 0 1 1160 640 V2902 Z" fill="url(#body-green)"/>

    <path class="inner-frame" d="M62 2850 V1200 A538 500 0 0 1 1138 1200 V2850 Z"
          fill="none" stroke="var(--frame-taupe)" stroke-width="12"/>

    <rect class="crest-art" x="240" y="250" width="720" height="410" rx="40"
          fill="url(#crest-tone)" opacity="0.85"
          role="img" aria-label="Crest illustration: star above two standing animals flanking a small shield"/>

    <path class="name-banner" d="M100 700 L220 665 Q600 640 980 665 L1110 700 L1040 740 L1100 790 L960 790 Q600 760 240 790 L100 790 L160 740 Z"
          fill="var(--banner-edge)"/>
    <path class="name-banner-inner" d="M235 675 Q600 652 965 675 L965 778 Q600 752 235 778 Z"
          fill="var(--banner-dark)"/>

    <path class="product-panel-frame" d="M118 1143 H1075 V1830 Q1075 2016 880 2016 H313 Q118 2016 118 1830 Z"
          fill="var(--frame-taupe)"/>
    <path class="product-panel" d="M140 1165 H1053 V1825 Q1053 1994 875 1994 H318 Q140 1994 140 1825 Z"
          fill="url(#panel-gold)"/>

    <ellipse class="olive-art" cx="390" cy="1610" rx="235" ry="215"
             fill="url(#olive-tone)"
             role="img" aria-label="Illustration of two green olives on a leafy sprig with floating oil droplets"/>
  </svg>

  <div class="text banner-name">BRINDELLA</div>

  <div class="text panel-name">BRINDELLA</div>
  <div class="text panel-product extra">EXTRA</div>
  <div class="text panel-product virgin">VIRGIN</div>
  <div class="panel-rule upper"></div>
  <div class="text panel-product olive">OLIVE</div>
  <div class="panel-rule lower"></div>
  <div class="text panel-product oil">OIL</div>

  <div class="text mandatory brand">BRINDELLA</div>
  <div class="text mandatory process">Cold Pressed</div>
  <div class="text mandatory product">EXTRA VIRGIN OLIVE OIL</div>
  <div class="text mandatory origin">AUSTRALIAN</div>

  <div class="text volume">1 litre</div>
</div>
</body>
</html>
```